Purchasing Management Consulting B to B Web Design PAYMENT GUARANTY

We'd like to build a new digital image for our website.

Our company is managing purchasing consultancy services for Large and Medium companies around 4 activities :
- Procurement outsourcing
- Purchasing consulting (cost reduction)
- Supply chain training
- Web platform to manage Supplier risk (TrovaNorm.com)

We now aim to harmonies our website in term of design in order to build a strongest Corporate Image.

SEE REQUIREMENT ENCLOSED

Please have a look on our current websites:
- www.kelpstrand.com
- www.qtr-network.com
- www.trovanorm.com

Reason: Hello, Some project received are not really professional and need more details. I did not see all deliverable requested in specifications. I'll revert to designer to improve design. Regards, Gaspard

Reason: Only few designers reply and feedback still need to be done.

Target Market(s)

Our business is exclusively Business to Business toward Medium and Large companies.

Industry/Entity Type

Digital

Requirements
Must have
• Website will be developped in Joomla CMS.
The user community will use Jomsocial module : Visitor should be "influenced" to communicate its contact details by registering the community.

Ergonomy, Simplicity and professionnalism is the key objectives.

Deliverables :
- Corporate Home page including clear access to our 4 activities
- Dynamique banner
- Corporate article / contact pages (1 or 2)
- Activities home pages (x 4)
- Activity Catalog (Indesign for paper version)
Nice to have
• Integration of Design for our consulting and training catalog will be interesting.

Livechat design (the one of Pixelharbor.com is good)
Should not have
• Only psd

Not html

```html
<!DOCTYPE html>
<html lang="fr">
<head>
<meta charset="utf-8">
<title>QTR – Purchasing Consulting</title>
<link href="https://fonts.googleapis.com/css2?family=Open+Sans:wght@300;400;700;800&family=Roboto:wght@400;500&display=swap" rel="stylesheet">
<style>
:root{
  --orange:#f66c00;
  --orange-light:#ff8d2a;
  --orange-deep:#ef5f00;
  --blue:#1c5a97;
  --blue-dark:#0d4a86;
  --check:#1f6fc4;
  --text:#555;
  --body:#333;
  --grey-line:#d9d9d9;
  --badge:#9a9a9a;
  --white:#fff;
}
*{box-sizing:border-box;margin:0;padding:0}
html,body{width:1200px;height:1050px;overflow:hidden;background:var(--white)}
body{position:relative;font-family:"Open Sans",sans-serif;color:var(--text)}
.hero{position:absolute;left:0;top:0;width:1200px;height:430px;
  background:
    radial-gradient(ellipse 180px 90px at 80px 200px,rgba(255,255,255,.55),transparent 70%),
    radial-gradient(ellipse 220px 80px at 1110px 250px,rgba(255,255,255,.6),transparent 70%),
    radial-gradient(ellipse 420px 260px at 560px 230px,var(--orange-light),transparent 80%),
    var(--orange)}
.hero-curve{position:absolute;left:0;top:0}
.top-tab{position:absolute;top:0;height:30px;background:rgba(255,255,255,.18);border:1px solid rgba(255,255,255,.45);border-top:none;border-radius:0 0 8px 8px}
.top-tab.newsletter{left:780px;width:94px;color:var(--white);font-size:10px;display:flex;align-items:center;justify-content:center;gap:5px}
.top-tab.social{width:24px}
.brand{position:absolute;display:flex;align-items:center;gap:8px;color:var(--white);font-weight:800;font-size:50px;letter-spacing:-1px}
.brand .dot{width:14px;height:14px;border-radius:50%;background:var(--white)}
.hero .brand{left:232px;top:62px}
.main-nav{position:absolute;left:425px;top:70px;display:flex;gap:15px;font-size:15px;font-weight:300;color:var(--white);letter-spacing:-.3px}
.main-nav span:last-child{margin-left:3px}
.hero-title{position:absolute;left:236px;top:228px;font-size:56px;font-weight:300;line-height:58px;color:var(--white);text-shadow:0 2px 3px rgba(0,0,0,.2)}
.invoice-art{position:absolute;left:616px;top:100px;width:314px;height:300px;border-radius:6px;
  background:linear-gradient(160deg,#ffffff 0%,#f2f2f2 70%,#ffe2c8 100%);box-shadow:0 6px 14px rgba(0,0,0,.2)}
.slider-dots{position:absolute;left:522px;top:372px;display:flex;gap:8px}
.slider-dots i{width:22px;height:22px;border-radius:50%;background:#eee;border:2px solid #ddd}
.slider-dots i.on{background:var(--white);border:5px solid var(--orange)}
.connect{position:absolute;left:238px;top:418px}
.connect h2{font-size:41px;font-weight:300;color:var(--blue);letter-spacing:-.5px}
.connect ul{list-style:none;margin-top:8px}
.connect li{display:flex;align-items:center;gap:8px;font-size:15px;font-weight:300;color:var(--text);height:29px}
.check{width:15px;height:15px;border-radius:3px;background:var(--check);display:flex;align-items:center;justify-content:center}
.tagline{position:absolute;left:608px;top:424px;width:360px;font-size:17px;font-weight:300;line-height:20px;color:var(--blue)}
.world-map{position:absolute;left:632px;top:472px;width:290px;height:132px;border-radius:40px;background:radial-gradient(ellipse at center,#ececec,#f6f6f6 70%,transparent)}
.partners{position:absolute;left:233px;top:611px;width:726px;height:99px;border:1px solid var(--grey-line);border-radius:3px;background:linear-gradient(#ffffff,#efefef)}
.partner-badges{position:absolute;left:28px;top:30px;display:flex;align-items:center;gap:26px}
.partner-badges b{display:block;background:var(--badge);opacity:.75;border-radius:4px;height:26px}
.partner-badges b.round{border-radius:50%;width:34px;height:34px}
.arrow-btn{position:absolute;top:74px;width:22px;height:22px;border-radius:50%;background:var(--white);border:1px solid #bbb;display:flex;align-items:center;justify-content:center}
.section-head{position:absolute;display:flex;align-items:center}
.section-head h3{font-size:22px;font-weight:400;color:var(--blue);letter-spacing:-.2px}
.view-all{position:absolute;width:67px;height:20px;background:var(--blue-dark);color:var(--white);font-family:Roboto,sans-serif;font-size:11px;display:flex;align-items:center;justify-content:center;border-radius:2px}
.news-item{position:absolute;left:262px;display:flex;gap:20px;font-family:Roboto,sans-serif;font-size:9px;line-height:16px;color:var(--body)}
.date{width:30px;height:28px;border:1.5px solid #666;text-align:center;font-family:"Open Sans",sans-serif;font-weight:700;font-size:13px;line-height:14px;color:#444;flex:none;margin-top:-1px}
.date small{display:block;font-size:5px;line-height:6px;letter-spacing:1px}
.bubble{position:absolute;left:632px;width:299px;height:70px;border:1px solid #ddd;border-radius:6px;background:var(--white);box-shadow:0 1px 3px rgba(0,0,0,.12);padding:10px 6px 0 14px;font-family:Roboto,sans-serif;font-size:9px;line-height:16px;color:var(--body)}
.bubble cite{display:block;margin-top:8px;font-style:normal;font-weight:500;color:#888}
.bubble::after{content:"";position:absolute;right:40px;bottom:-9px;width:16px;height:16px;background:var(--white);border-right:1px solid #ddd;border-bottom:1px solid #ddd;transform:rotate(45deg)}
.footer{position:absolute;left:0;top:964px;width:1200px;height:86px;border-top:1px solid #ccc;background:linear-gradient(#ececec,#fafafa 40%,#fff)}
.footer-links{position:absolute;left:249px;top:30px;font-family:Roboto,sans-serif;font-size:9px;color:#888}
.footer-links span{margin:0 5px}
.copyright{position:absolute;left:249px;top:51px;font-family:Roboto,sans-serif;font-size:9px;color:#444}
.footer-social{position:absolute;left:682px;top:36px;display:flex;gap:11px}
.footer-social i{width:21px;height:21px;border-radius:50%;border:1.5px solid #777}
.footer .brand{left:842px;top:22px;color:var(--blue);font-size:30px}
.footer .brand .dot{background:var(--blue);width:9px;height:9px}
</style>
</head>
<body>

<header class="hero">
  <svg class="hero-curve" width="1200" height="440" viewBox="0 0 1200 440" aria-hidden="true">
    <path d="M0 420 Q600 332 1200 420 L1200 440 L0 440 Z" fill="#fff"/>
  </svg>

  <div class="top-tab newsletter">
    <svg width="11" height="9" viewBox="0 0 11 9" aria-hidden="true"><rect x=".5" y=".5" width="10" height="8" fill="none" stroke="#fff"/><path d="M.5 .5 L5.5 5 L10.5 .5" fill="none" stroke="#fff"/></svg>
    Newsletter
  </div>
  <div class="top-tab social" style="left:882px"></div>
  <div class="top-tab social" style="left:911px"></div>
  <div class="top-tab social" style="left:941px"></div>

  <div class="brand"><span class="dot"></span>QTR</div>

  <nav class="main-nav">
    <span>ACCUEIL</span><span>TROVANORM.COM</span><span>KELP STRAND</span><span>NOUS CONTACTER</span><span>NEWSLETTER</span>
  </nav>

  <h1 class="hero-title">Purchasing<br>Consulting</h1>

  <div class="invoice-art" role="img" aria-label="Illustration of a paper invoice surrounded by a calculator, hourglass, money bag and credit card icons"></div>

  <div class="slider-dots"><i></i><i class="on"></i><i></i><i></i></div>
</header>

<section class="connect">
  <h2>Rester connecter!</h2>
  <ul>
    <li><span class="check"><svg width="9" height="8" viewBox="0 0 9 8"><path d="M1 4 L3.5 6.5 L8 1" fill="none" stroke="#fff" stroke-width="1.8"/></svg></span>Connectez-vous et agrandissez votre réseau</li>
    <li><span class="check"><svg width="9" height="8" viewBox="0 0 9 8"><path d="M1 4 L3.5 6.5 L8 1" fill="none" stroke="#fff" stroke-width="1.8"/></svg></span>Voir les profils et ajouter de nouveaux contacts</li>
    <li><span class="check"><svg width="9" height="8" viewBox="0 0 9 8"><path d="M1 4 L3.5 6.5 L8 1" fill="none" stroke="#fff" stroke-width="1.8"/></svg></span>Partagez vos réalisations, photos et vidéos.</li>
    <li><span class="check"><svg width="9" height="8" viewBox="0 0 9 8"><path d="M1 4 L3.5 6.5 L8 1" fill="none" stroke="#fff" stroke-width="1.8"/></svg></span>Créez vos propres groupes ou rejoignez en d'autres</li>
  </ul>
</section>

<p class="tagline">Un réseau de partenaires intégrés, dédié à la réduction des coûts.</p>
<div class="world-map" role="img" aria-label="Faint grey world map"></div>

<section class="partners">
  <div class="partner-badges">
    <b style="width:62px"></b>
    <b class="round"></b>
    <b style="width:92px"></b>
    <b class="round"></b>
    <b style="width:100px"></b>
    <b style="width:56px"></b>
    <b style="width:76px"></b>
    <b class="round"></b>
  </div>
  <span class="arrow-btn" style="left:7px"><svg width="7" height="9" viewBox="0 0 7 9"><path d="M5.5 1 L2 4.5 L5.5 8" fill="none" stroke="#222" stroke-width="2"/></svg></span>
  <span class="arrow-btn" style="left:695px"><svg width="7" height="9" viewBox="0 0 7 9"><path d="M1.5 1 L5 4.5 L1.5 8" fill="none" stroke="#222" stroke-width="2"/></svg></span>
</section>

<div class="section-head" style="left:261px;top:740px">
  <svg width="39" height="38" viewBox="0 0 39 38" aria-hidden="true"><rect x="4" y="1" width="33" height="35" fill="none" stroke="#666" stroke-width="2"/><path d="M4 8 H1 V36 H4" fill="none" stroke="#666" stroke-width="2"/><rect x="9" y="6" width="10" height="9" fill="none" stroke="#666" stroke-width="1.5"/><path d="M22 7H32M22 11H32M22 15H32M9 20H32M9 24H32M9 28H32M9 32H32" stroke="#666" stroke-width="1.5"/></svg>
  <h3 style="margin-left:18px">NEWS / EVENT</h3>
</div>
<span class="view-all" style="left:512px;top:749px">View All</span>

<div class="news-item" style="top:800px"><div class="date">20<small>FEB</small></div><p>Lorem ipsum dolor sit amet, consectetuer adipiscing elit,<br>sed diam nonummy nibh euismod tincidunt ut laoreet<br>dolore magna.</p></div>
<div class="news-item" style="top:854px"><div class="date">20<small>FEB</small></div><p>Lorem ipsum dolor sit amet, consectetuer adipiscing elit, sed diam<br>nonummy nibh euismod tincidunt ut laoreet dolore magna.</p></div>
<div class="news-item" style="top:904px"><div class="date">20<small>FEB</small></div><p>Lorem ipsum dolor sit amet, consectetuer adipiscing elit, sed<br>diam nonummy nibh euismod tincidunt ut laoreet dolore<br>magna.</p></div>

<div class="section-head" style="left:625px;top:740px">
  <svg width="38" height="38" viewBox="0 0 38 38" aria-hidden="true"><path d="M6 26 L27 5 L33 11 L12 32 L4 35 Z" fill="none" stroke="#666" stroke-width="2" stroke-linejoin="round"/><path d="M24 8 L30 14M6 26 L12 32" stroke="#666" stroke-width="2"/></svg>
  <h3 style="margin-left:11px">TESTIMONIALS</h3>
</div>
<span class="view-all" style="left:864px;top:749px">View All</span>

<blockquote class="bubble" style="top:788px">"Lorem ipsum dolor sit amet, consectetuer adipiscing elit, sed diam nonummy nibh euismod tincidunt ut laoreet dolore magna."<cite>— Hal Brennick</cite></blockquote>
<blockquote class="bubble" style="top:876px">"Lorem ipsum dolor sit amet, consectetuer adipiscing elit, sed diam nonummy nibh euismod tincidunt ut laoreet dolore magna."<cite>— Hal Brennick</cite></blockquote>

<footer class="footer">
  <p class="footer-links">Kelp Strand<span>|</span>Recruitment<span>|</span>Press<span>|</span>Imprint<span>|</span>Contact Us</p>
  <p class="copyright">© 2013 TrovaNorm Ltd - All Rights Reserved.</p>
  <div class="footer-social"><i></i><i></i><i></i></div>
  <div class="brand"><span class="dot"></span>QTR</div>
</footer>

</body>
</html>
```